Harbor of Kitchencraft Podcast Episode Cover

I’m looking for a clean, professional, and eye-catching podcast episode cover template for my show, Harbor of Kitchencraft. Each week, I feature a new guest, so the design must allow me (or my team) to easily swap in a new guest’s photo without needing advanced design skills.

The template should be:

- Drag-and-drop friendly: simple for me to replace the guest’s headshot in Canva, Photoshop, or similar.
- On-brand with the Harbor of Kitchencraft podcast: professional yet approachable, foodservice industry-focused.
- Bold and attention-grabbing for podcast platforms and social media.

Readable text at small sizes, since covers are often viewed as thumbnails.

Design Elements to Include:

1. Podcast Title: “Harbor of Kitchencraft” (prominently displayed)
2. Subtitle/Space: Line for guest’s name, professional title, and company name
3. Photo Placeholder: Large, central area where I can easily drag and drop a guest photo
4. Brand Colors: attached
5. Clean, modern fonts (easy to read at thumbnail size)
6. Background graphics or patterns that give a sense of foodservice, leadership, or nationwide reach... but do not overpower the guest photo

Format Requirements:

- Editable source file (PSD, Canva template, or layered AI/INDD)
- JPG/PNG exports for immediate use
- Square format (3000x3000px) for podcast platforms

Style Inspiration:
Think modern podcast covers: bold fonts, clean lines, professional with a touch of energy.

Deliverables:

1. Final episode cover template (editable file)
2. Instructions or guidance on how to swap out guest photos

```html
<!DOCTYPE html>
<html lang="en">
<head>
<meta charset="utf-8">
<title>Harbor of Kitchencraft – Episode Cover</title>
<link href="https://fonts.googleapis.com/css2?family=Bebas+Neue&family=Oswald:wght@600&display=swap" rel="stylesheet">
<style>
  :root {
    --navy: #1e3a50;
    --gold: #f7b716;
    --white: #ffffff;
    --photo-placeholder: #e5e5e5;
  }
  html, body {
    margin: 0;
    padding: 0;
    width: 1200px;
    height: 1200px;
    overflow: hidden;
    background: var(--gold);
  }
  .episode-cover {
    display: block;
    width: 1200px;
    height: 1200px;
  }
  .cover-base { fill: var(--gold); }
  .title-band { fill: var(--navy); }
  .stop-gold { stop-color: var(--gold); }
  .stop-navy { stop-color: var(--navy); }
  .show-title {
    font-family: "Bebas Neue", "Oswald", sans-serif;
  }
  .show-title-top { fill: var(--white); font-size: 312px; }
  .show-title-bottom { fill: var(--gold); font-size: 262px; }
  .photo-ring { fill: var(--white); }
  .guest-photo { fill: var(--photo-placeholder); }
  .guest-info {
    font-family: "Oswald", sans-serif;
    font-weight: 600;
    fill: var(--navy);
  }
  .guest-name { font-size: 92px; }
  .guest-role, .guest-company { font-size: 58px; }
</style>
</head>
<body>
<svg class="episode-cover" viewBox="0 0 1200 1200" xmlns="http://www.w3.org/2000/svg">
  <defs>
    <linearGradient id="top-fade" x1="0" y1="0" x2="0" y2="1">
      <stop class="stop-gold" offset="0"/>
      <stop class="stop-navy" offset="1"/>
    </linearGradient>
    <linearGradient id="lower-fade" x1="0" y1="0" x2="0" y2="1">
      <stop class="stop-navy" offset="0"/>
      <stop class="stop-gold" offset="1"/>
    </linearGradient>
  </defs>

  <rect class="cover-base" x="0" y="0" width="1200" height="1200"/>

  <!-- title band -->
  <rect class="title-band" x="0" y="0" width="1200" height="640"/>

  <!-- decorative pattern areas -->
  <rect x="0" y="0" width="1200" height="108" fill="url(#top-fade)" role="img" aria-label="Decorative dot pattern area, gold on navy"/>
  <rect x="0" y="640" width="1200" height="176" fill="url(#lower-fade)" role="img" aria-label="Decorative dot pattern area, navy on gold"/>

  <!-- show title -->
  <text class="show-title show-title-top" x="144" y="354" textLength="918" lengthAdjust="spacingAndGlyphs">HARBOR OF</text>
  <text class="show-title show-title-bottom" x="77" y="574" textLength="1053" lengthAdjust="spacingAndGlyphs">KITCHENCRAFT</text>

  <!-- guest photo slot -->
  <circle class="photo-ring" cx="352" cy="882" r="290"/>
  <circle class="guest-photo" cx="352" cy="882" r="275" role="img" aria-label="Guest headshot placeholder – drop the guest's photo here"/>

  <!-- guest details -->
  <g class="guest-info">
    <text class="guest-name" x="668" y="1006" textLength="464" lengthAdjust="spacingAndGlyphs">Guest’s Name</text>
    <text class="guest-role" x="668" y="1076" textLength="334" lengthAdjust="spacingAndGlyphs">Professional Title</text>
    <text class="guest-company" x="668" y="1136" textLength="450" lengthAdjust="spacingAndGlyphs">Guest’s Company Name</text>
  </g>
</svg>
</body>
</html>
```